Offshore Energy Projects Management Consultancy needs a business card design

Logo available. We provide teams to deliver engineering consultancy, project management and delivery teams mainly in the offshore renewables sector. The company is all about bringing the right people to a project to deliver the scope.

The business card will be used for all staff.

The business card should be quite simple, vibrant and uncluttered but convey experience, enthusiasm and integration.

Target Market(s)

Energy Project Developers and Tier 1 construction companies

Contact Information for Business Card

Logo should be on the back of the card. I'm happy for the designer to play with the colour of the logo and background colour.

Front of the card should convey all the must have information in a clear and professional manner but without being overly traditional.

Colors

Designer to choose colors to be used in the design.

Requirements
Must have
• Land Line Tel Number, Mobile Tel Number, Email, business address, web address.

```html
<!DOCTYPE html>
<html lang="en">
<head>
<meta charset="UTF-8">
<title>Tidewell Project Partners – Business Card</title>
<link href="https://fonts.googleapis.com/css2?family=Oswald:wght@300;400;600&display=swap" rel="stylesheet">
<style>
  :root {
    --canvas: #d9d9d9;
    --card-white: #f1f1f0;
    --blue-light: #3d68a8;
    --blue-deep: #0c1a33;
    --ink: #262626;
    --ink-muted: #888a8c;
    --accent: #3463b4;
    --rule: #2b2b2b;
  }
  * { box-sizing: border-box; margin: 0; padding: 0; }
  html, body {
    width: 1200px; height: 1200px; overflow: hidden;
    background: var(--canvas);
    font-family: 'Oswald', sans-serif;
  }
  .canvas {
    position: relative; width: 1200px; height: 1200px;
    display: flex; flex-direction: column; align-items: center;
    justify-content: center; gap: 60px;
  }
  .card {
    position: relative; width: 700px; height: 400px;
    box-shadow: 0 6px 18px rgba(0,0,0,0.18);
    overflow: hidden;
  }
  /* Back of card */
  .card--back {
    background: radial-gradient(ellipse at 62% 60%, var(--blue-light) 0%, #2f5591 45%, var(--blue-deep) 100%);
    display: flex; align-items: center; justify-content: center;
  }
  .brand-back {
    display: flex; align-items: center; gap: 18px;
    color: #0d1626; font-weight: 600; font-size: 40px;
    letter-spacing: 3px; text-transform: uppercase;
  }
  .brand-back .brand-square {
    width: 34px; height: 34px; background: #0d1626;
  }
  /* Front of card */
  .card--front { background: var(--card-white); }
  .front-header {
    position: absolute; left: 0; right: 40px; top: 88px;
    display: flex; align-items: center; gap: 22px;
  }
  .front-rule {
    flex: 1; height: 2px; background: var(--rule);
    margin-top: 14px;
  }
  .brand-front {
    display: flex; align-items: center; gap: 12px; flex: none;
    color: var(--accent); font-weight: 600; font-size: 24px;
    letter-spacing: 2px; text-transform: uppercase; line-height: 1;
  }
  .brand-front .brand-square { width: 20px; height: 20px; background: var(--accent); }
  .person { position: absolute; left: 64px; top: 212px; }
  .person-name {
    font-weight: 600; font-size: 34px; letter-spacing: 3px;
    color: var(--ink); text-transform: uppercase; line-height: 1.05;
  }
  .person-title {
    font-weight: 400; font-size: 22px; letter-spacing: 4px;
    color: var(--accent); text-transform: uppercase;
  }
  .contacts {
    position: absolute; left: 64px; top: 300px; right: 40px;
    font-weight: 300; font-size: 21px; letter-spacing: 1.5px;
    color: var(--ink); line-height: 1.75;
  }
  .contact-row { display: flex; align-items: baseline; gap: 14px; white-space: nowrap; }
  .contact-label { color: var(--accent); font-weight: 400; margin-right: 4px; }
  .contact-sep { color: var(--ink); margin: 0 6px; }
</style>
</head>
<body>
<main class="canvas">
  <section class="card card--back" aria-label="Card back">
    <div class="brand-back"><span class="brand-square"></span><span>Tidewell Project Partners</span></div>
  </section>

  <section class="card card--front" aria-label="Card front">
    <div class="front-header">
      <div class="front-rule"></div>
      <div class="brand-front"><span class="brand-square"></span><span>Tidewell Project Partners</span></div>
    </div>

    <div class="person">
      <h1 class="person-name">John Smith</h1>
      <p class="person-title">Title Here</p>
    </div>

    <div class="contacts">
      <div class="contact-row">
        <span><span class="contact-label">P.</span>123.456.7890</span>
        <span class="contact-sep">|</span>
        <span><span class="contact-label">P.</span>123.456.7889</span>
        <span class="contact-sep">|</span>
        <span><span class="contact-label">E.</span>john@yourweb.com</span>
      </div>
      <div class="contact-row">
        <span><span class="contact-label">A.</span>123 Main St. Your City, TX. 01234</span>
      </div>
    </div>
  </section>
</main>
</body>
</html>
```